Website design for an events management company

What we need is the design of a website to be used by an events management company, the company is called "Velto Conference Services" and the website is expected to contain the following sections:
1) Homepage
2) Who are we?
3) Mission / Vision / Core values
4) Why to choose Velto?
5) Past experience
6) Duties or provided services (Scientific Program Duties, Accreditation, Fund Raising, Accommodations, Social Activities, Transportation, Marketing of the Event, Publications and printed materials, Secretarial Work and Media Coverage)
7) References
8) Contact Us page (will probably contain a contact us form plus email, address and a google map)

Attached for your reference the company's logo

Expected that the winner should deliver the designs of at least two pages (the homepage plus an inner page) plus of course all the used graphics, images ... etc.

Thanks

Target Market(s)

The design need to target scientific events and not public events, for example the company doesn't organize music concerts ... etc., it organizes only scientific events so please target business users (i.e. doctors, engineers, scientisits ... etc) while making the designs, including the correct colors, images and icons

Industry/Entity Type

It Company

Number of Pages Required

2 page

Requirements
Must have
• One homepage
• One inner page
• All the used graphics and images
Nice to have
• More than two pages

```html
<!DOCTYPE html>
<html lang="en">
<head>
<meta charset="utf-8">
<title>Velto Conference Services — Home</title>
<link rel="stylesheet" href="https://fonts.googleapis.com/css2?family=Cousine&family=Open+Sans:wght@400;600&family=Open+Sans+Condensed:ital,wght@1,700&family=Pinyon+Script&display=swap">
<style>
  :root {
    --orange: #f26a1b;
    --navy: #1c2a5c;
    --white: #ffffff;
    --footer-grey: #e3e3e3;
    --social-blue: #3b5b9a;
    --social-sky: #4fa8de;
  }
  * { margin: 0; padding: 0; box-sizing: border-box; }
  html, body { width: 1200px; height: 812px; overflow: hidden; background: var(--white); }
  .page { position: relative; width: 1200px; height: 812px; overflow: hidden; font-family: "Open Sans", sans-serif; color: var(--navy); }

  .site-header { position: absolute; top: 0; left: 0; width: 1200px; height: 116px; background: var(--white); z-index: 2; }
  .brand { position: absolute; left: 45px; top: 13px; width: 86px; height: 86px; border: 6px solid var(--orange); border-radius: 50%;
           display: flex; align-items: center; justify-content: center; font-family: "Open Sans", sans-serif; font-weight: 600; font-size: 19px; color: var(--navy); }
  .main-nav { position: absolute; top: 0; left: 0; width: 1200px; height: 116px; }
  .nav-link { position: absolute; top: 50px; font-family: "Cousine", monospace; font-size: 15px; letter-spacing: 0.3px; color: var(--navy); text-decoration: none; white-space: nowrap; }
  .nav-link.is-active { color: var(--orange); }
  .nav-divider { position: absolute; top: 44px; width: 2px; height: 29px; background: var(--orange); }

  .header-edge { position: absolute; top: 112px; left: 0; width: 1200px; height: 24px; z-index: 3; }

  .hero { position: absolute; top: 116px; left: 0; width: 1200px; height: 472px;
          background:
            linear-gradient(180deg, rgba(230,232,236,0.95) 0%, rgba(214,212,206,0.85) 30%, rgba(150,110,90,0.9) 62%, rgba(90,60,55,1) 100%),
            linear-gradient(90deg, #cfd6df 0%, #e8e4dc 50%, #d8b890 100%); }
  .hero-title { position: absolute; top: 180px; left: 0; width: 1200px; text-align: center; font-family: "Pinyon Script", cursive;
                font-size: 62px; color: var(--navy); word-spacing: 14px; z-index: 2; }

  .intro { position: absolute; top: 608px; left: 150px; width: 900px; text-align: center; font-size: 16.5px; line-height: 20px; color: var(--navy); }
  .intro-quote { font-family: "Open Sans Condensed", sans-serif; font-style: italic; font-weight: 700; font-size: 20px; }

  .site-footer { position: absolute; left: 0; top: 730px; width: 1200px; height: 82px; }
  .social-list { position: absolute; right: 80px; top: 770px; display: flex; gap: 22px; list-style: none; }
  .social-item { display: flex; align-items: center; gap: 7px; font-size: 15px; font-weight: 600; color: var(--navy); }
  .social-square { width: 22px; height: 22px; }
  .social-square.sky { background: var(--social-sky); }
  .social-square.blue { background: var(--social-blue); }
</style>
</head>
<body>
<div class="page">
  <header class="site-header">
    <div class="brand">Velto</div>
    <nav class="main-nav">
      <a class="nav-link is-active" href="#" style="left:186px">HOME</a>
      <span class="nav-divider" style="left:258px"></span>
      <a class="nav-link" href="#" style="left:295px">ABOUT US</a>
      <span class="nav-divider" style="left:397px"></span>
      <a class="nav-link" href="#" style="left:427px">MISSION</a>
      <span class="nav-divider" style="left:510px"></span>
      <a class="nav-link" href="#" style="left:526px">WHY CHOOSE US</a>
      <span class="nav-divider" style="left:660px"></span>
      <a class="nav-link" href="#" style="left:677px">SERVICES</a>
      <span class="nav-divider" style="left:759px"></span>
      <a class="nav-link" href="#" style="left:767px">PAST EXPERIENCES</a>
      <span class="nav-divider" style="left:917px"></span>
      <a class="nav-link" href="#" style="left:922px">REFERENCES</a>
      <span class="nav-divider" style="left:1031px"></span>
      <a class="nav-link" href="#" style="left:1049px">CONTACT US</a>
    </nav>
  </header>

  <svg class="header-edge" viewBox="0 0 1200 24" preserveAspectRatio="none" aria-hidden="true">
    <path d="M0 0 L0 3 Q300 6 590 18 L600 14 L610 18 Q900 6 1200 3 L1200 0 Z" fill="#ffffff"/>
    <path d="M0 3 Q300 6 590 18 L600 14 L610 18 Q900 6 1200 3" fill="none" stroke="#f26a1b" stroke-width="2.5"/>
  </svg>

  <section class="hero" role="img" aria-label="Photo of an audience seated in rows facing a projection screen at a conference hall"></section>
  <h1 class="hero-title">Be positive ... Be creative</h1>

  <p class="intro">As Arthur Pembridge once said: <span class="intro-quote">“the price of greatness is responsibility over each of your thoughts”</span>. Being positive is our commitment to making a positive difference in the world. Through redesigning the way we work and live. As we act with an eye toward future generations, we focus on driving business growth and helping to create a more sustainable world</p>

  <svg class="site-footer" viewBox="0 0 1200 82" preserveAspectRatio="none" aria-hidden="true">
    <path d="M0 22 Q600 -14 1200 22 L1200 82 L0 82 Z" fill="#e3e3e3"/>
  </svg>
  <ul class="social-list">
    <li class="social-item"><span class="social-square sky"></span>Postwave</li>
    <li class="social-item"><span class="social-square blue"></span>Friendhub</li>
  </ul>
</div>
</body>
</html>
```